Design/Layout (PowerPoint Master) für Broschüre
Zielgruppe
VARELTO Management Consulting ist eine Unternehmensberatung mit Sitz in Köln. Für unser Recruiting möchten wir eine (DIN A6 quer) Broschüre erstellen, die Beratern kurz nach Vertragsunterzeichnung zugesendet wird mit den wichtigsten Infos zu Ihrer künftigen Arbeit bei uns. Ein paar (teilweise Dummy) Slides gibt es schon. Mehr Inhalt wird aktuell von uns generiert. Es geht bei der Aufgabe nur darum, das Design zu erstellen, es muss kein Inhalt selbst erstellt werden. Eine aktuelle Version der Broschüre ist hier zu finden. Als Orientierung sollte das neue Design unserer Website (PNG-Datei) dienen.
Aufgabenstellung
Die Broschüre soll A6 Format (quer) haben. Wir benötigen sie im PowerPoint Format, damit wir selbst noch Inhalt generieren bzw. den Inhalt bearbeiten können.
Wir hätten je Seite gerne eine Überschrift, sowie Kapitel (und Übersichtsseiten). Schriftart wäre Arial. Gerne hätten wir einen Footer mit Seitenzahl. Könnten Sie sich wegen des Designs an unserer neuen (gerade in Arbeit) Homepage orientieren (die Startseite ist als PNG im Anhang).

```html
<!DOCTYPE html>
<html lang="de">
<head>
<meta charset="utf-8">
<title>VARELTO Onboarding Broschüre</title>
<link href="https://fonts.googleapis.com/css2?family=Arimo:ital,wght@0,400;0,700;1,700&display=swap" rel="stylesheet">
<style>
  :root{
    --red:#b3232a;
    --black:#1d1d1d;
    --ink:#222222;
    --paper:#f4f4f4;
    --paper-shade:#e2e2e2;
    --stage:#d9d9d9;
    --white:#ffffff;
    --photo-dark:#2b1d1c;
    --photo-red:#8e3a32;
    --photo-grey:#7a7a7a;
  }
  *{margin:0;padding:0;box-sizing:border-box}
  html,body{width:1200px;height:2400px;overflow:hidden}
  body{background:var(--stage);font-family:"Arimo",Arial,sans-serif;color:var(--ink);position:relative}

  .page{position:absolute;overflow:hidden;background:var(--paper)}
  .spread{position:absolute;left:40px;width:1120px;height:396px;box-shadow:0 6px 18px rgba(0,0,0,.18)}
  .spread .page{top:0;width:560px;height:396px}
  .spread .page.left{left:0;background:linear-gradient(90deg,var(--paper) 0%,var(--paper) 82%,var(--paper-shade) 100%)}
  .spread .page.right{left:560px;background:linear-gradient(90deg,var(--paper-shade) 0%,var(--paper) 14%,var(--paper) 100%)}
  .abs{position:absolute}

  /* cover */
  .cover{left:303px;top:60px;width:594px;height:420px;background:var(--white);box-shadow:0 6px 18px rgba(0,0,0,.18)}
  .cover-band{position:absolute;left:0;right:0;top:270px;bottom:0;background:var(--black)}
  .cover-rule{position:absolute;left:0;right:0;top:254px;height:5px;background:var(--red)}
  .brand-name{position:absolute;left:30px;top:24px;font-size:30px;font-weight:700;letter-spacing:1px;color:var(--ink)}
  .cover-title{position:absolute;left:446px;top:340px;color:var(--white);font-weight:700;font-size:18px;line-height:1.3}
  .cover-title-rule{position:absolute;left:384px;top:357px;width:48px;height:2px;background:var(--white)}
  .cover svg{position:absolute;left:0;top:0}

  /* shared type */
  .heading-dash{display:inline-block;width:32px;height:2px;background:currentColor;vertical-align:middle;margin-right:8px}
  .kicker{font-weight:700;font-size:13px;color:var(--red)}
  .copy{font-size:9px;line-height:1.45;color:var(--ink)}
  .page-rule{position:absolute;height:1.5px;background:var(--red)}
  .page-number{position:absolute;width:26px;height:26px}

  /* contents */
  .toc-title{left:40px;top:56px;font-weight:700;font-size:18px}
  .toc-col{width:230px}
  .toc-item{display:flex;align-items:baseline;font-weight:700;font-size:11px;margin-bottom:7px}
  .toc-item .num{width:20px;flex:none}
  .toc-item .leader{flex:1;border-bottom:1px dotted #777;margin:0 4px}
  .toc-item .pg{color:var(--red);font-size:8px}
  .toc-sub{font-weight:400;font-size:8.5px;line-height:1.35;margin:-4px 0 7px 20px;color:#444}
  .bottom-band{position:absolute;left:0;right:0;bottom:0;height:5px;background:var(--red)}

  .quote-text{left:150px;top:180px;width:260px;text-align:center;color:var(--white);font-style:italic;font-weight:700;font-size:22px;line-height:1.15}
  .quote-mark{left:240px;top:96px;width:80px;text-align:center;color:var(--white);font-weight:700;font-size:86px;line-height:1}
  .quote-rule{left:248px;top:262px;width:64px;height:2px;background:var(--red)}

  .section-title{font-weight:700;font-size:22px}
  .lead{font-weight:700;font-size:13.5px;line-height:1.5}

  .photo-hero{position:absolute;left:0;top:0;width:560px;height:396px;
    background:radial-gradient(ellipse at 60% 30%,#5a3a3a 0%,transparent 55%),linear-gradient(160deg,#2a2222 0%,#6d3530 45%,#9a4a3f 75%,#7a3a33 100%)}
  .hero-shade{position:absolute;left:0;right:0;bottom:0;height:60%;background:linear-gradient(180deg,transparent,rgba(40,15,15,.55))}
  .hero-kicker{left:40px;top:160px;color:var(--white);font-weight:700;font-size:20px}
  .hero-headline{left:40px;top:250px;width:470px;color:var(--white);font-weight:700;font-size:27px;line-height:1.18}
  .intro-bold{font-weight:700;font-size:9.5px;line-height:1.45}
</style>
</head>
<body>

<!-- Cover -->
<section class="page cover">
  <div class="cover-rule"></div>
  <div class="cover-band"></div>
  <div class="brand-name">VARELTO</div>
  <svg width="594" height="420" viewBox="0 0 594 420">
    <defs>
      <linearGradient id="coverPhoto" x1="0" y1="0" x2="0" y2="1">
        <stop offset="0" stop-color="#3a2f2f"/>
        <stop offset="0.45" stop-color="#6a3b35"/>
        <stop offset="1" stop-color="#a8463c"/>
      </linearGradient>
    </defs>
    <polygon points="297,54 422,126 422,266 297,338 172,266 172,126" fill="url(#coverPhoto)" stroke="#ffffff" stroke-width="3" role="img" aria-label="Foto: Sprinter im Startblock auf roter Laufbahn"/>
  </svg>
  <div class="cover-title-rule"></div>
  <div class="cover-title">Onboarding<br>Broschüre</div>
</section>

<!-- Spread: Zitat + Inhalt -->
<section class="spread" style="top:560px">
  <div class="page left">
    <svg class="abs" style="left:0;top:0" width="560" height="396" viewBox="0 0 560 396">
      <polygon points="180,105 380,90 450,200 370,320 165,330 110,215" fill="#1d1d1d"/>
    </svg>
    <div class="abs quote-mark">”</div>
    <div class="abs quote-text">Konzepte sind<br>nicht alles.</div>
    <div class="abs quote-rule"></div>
    <div class="bottom-band"></div>
  </div>
  <div class="page right">
    <div class="abs toc-title"><span class="heading-dash"></span>Inhalt</div>
    <div class="abs toc-col" style="left:40px;top:100px">
      <div class="toc-item"><span class="num">1.</span>Portfolio-Schärfung<span class="leader"></span><span class="pg">4</span></div>
      <div class="toc-sub">serum si con nes sin reium quo ma<br>accus et quamus molo</div>
      <div class="toc-item"><span class="num">2.</span>Outsourcing<span class="leader"></span><span class="pg">6</span></div>
      <div class="toc-item"><span class="num">3.</span>Transparenz<span class="leader"></span><span class="pg">8</span></div>
      <div class="toc-item"><span class="num">4.</span>Management-Conventions<span class="leader"></span><span class="pg">10</span></div>
      <div class="toc-sub">rrovid modigni optis neculparibus<br>doluptatio. Git eaturiosant doluptate<br>remqui comnis velestrum</div>
      <div class="toc-item"><span class="num">5.</span>Mitarbeiter Feedack<span class="leader"></span><span class="pg">12</span></div>
      <div class="toc-item"><span class="num">6.</span>IT-Security<span class="leader"></span><span class="pg">14</span></div>
      <div class="toc-item"><span class="num">7.</span>Integrationen<span class="leader"></span><span class="pg">16</span></div>
    </div>
    <div class="abs toc-col" style="left:300px;top:60px">
      <div class="toc-item"><span class="num">8.</span>Change-Programme<span class="leader"></span><span class="pg">18</span></div>
      <div class="toc-item"><span class="num">9.</span>Performance-Management<span class="leader"></span><span class="pg">20</span></div>
      <div class="toc-sub">rrovid modigni optis neculparibus<br>doluptatio. Git eaturiosant doluptate<br>remqui comnis velestrum</div>
      <div class="toc-item"><span class="num">10.</span>Mitarbeiter-Events<span class="leader"></span><span class="pg">22</span></div>
      <div class="toc-item"><span class="num">11.</span>Unternehmenskommunikation<span class="leader"></span><span class="pg">24</span></div>
    </div>
    <div class="bottom-band"></div>
  </div>
</section>

<!-- Spread: Portfolio-Schärfung -->
<section class="spread" style="top:1036px">
  <div class="page left">
    <div class="abs section-title" style="left:40px;top:70px"><span class="heading-dash"></span>Portfolio-Schärfung</div>
    <p class="abs lead" style="left:40px;top:240px;width:340px">Utem aut porumet labore doluptas aliquat ilignias et aut voluptati rem a dipsam eum harumquature quo quis magnameniti optatius delecepra volupis con pere num,</p>
    <div class="page-rule" style="left:40px;top:352px;width:520px"></div>
    <svg class="page-number" style="left:390px;top:339px" viewBox="0 0 26 26"><polygon points="13,1 24,7 24,19 13,25 2,19 2,7" fill="#1d1d1d"/><text x="13" y="16.5" font-size="9" font-weight="700" fill="#fff" text-anchor="middle" font-family="Arimo, Arial, sans-serif">4</text></svg>
  </div>
  <div class="page right">
    <div class="abs" style="left:40px;top:236px;width:230px">
      <div class="kicker"><span class="heading-dash"></span>Überschrift</div>
      <p class="copy" style="margin-top:8px">Utem aut porumet labore doluptas aliquat ilignias et aut voluptati rem a dipsam eum harumquature quo quis magnameniti optatius delecepra volupis con pere num, ommolor atemoli icimusam quiamus quaepud iatior sum quis amus iduci as acit ut odigend uciamet</p>
    </div>
    <div class="abs" style="left:300px;top:200px;width:230px">
      <div class="kicker"><span class="heading-dash"></span>Überschrift</div>
      <p class="copy" style="margin-top:8px">Utem aut porumet labore doluptas aliquat ilignias et aut voluptati rem a dipsam eum harumquature quo quis magnameniti optatius delecepra volupis con pere num, ommolor atemoli icimusam quiamus quaepud iatior sum quis amus iduci as acit ut odigend uciamet. Utem aut porumet labore doluptas aliquat aut voluptati rem a dipsam eum harum.</p>
    </div>
    <div class="page-rule" style="left:0;top:352px;width:520px"></div>
    <svg class="page-number" style="left:340px;top:339px" viewBox="0 0 26 26"><polygon points="13,1 24,7 24,19 13,25 2,19 2,7" fill="#1d1d1d"/><text x="13" y="16.5" font-size="9" font-weight="700" fill="#fff" text-anchor="middle" font-family="Arimo, Arial, sans-serif">5</text></svg>
  </div>
  <svg class="abs" style="left:0;top:0" width="1120" height="396" viewBox="0 0 1120 396">
    <defs>
      <linearGradient id="runnersPhoto" x1="0" y1="0" x2="1" y2="1">
        <stop offset="0" stop-color="#9a9a9a"/>
        <stop offset="0.5" stop-color="#3c3c3c"/>
        <stop offset="1" stop-color="#1e1e1e"/>
      </linearGradient>
    </defs>
    <polygon points="420,40 1120,0 1120,172 700,222 660,222 420,180" fill="url(#runnersPhoto)" role="img" aria-label="Schwarz-Weiß-Foto: Läufer im Wettkampf auf der Bahn"/>
  </svg>
</section>

<!-- Spread: Strategie -->
<section class="spread" style="top:1512px">
  <div class="page left">
    <div class="photo-hero" role="img" aria-label="Foto: Laufschuh auf roter Tartanbahn"></div>
    <div class="hero-shade"></div>
    <div class="abs hero-kicker"><span class="heading-dash"></span>Überschrift</div>
    <div class="abs hero-headline">Ein Strategie- und Organisationsprojekt kann viel bewegen und verändern</div>
  </div>
  <div class="page right">
    <div class="abs kicker" style="left:200px;top:40px"><span class="heading-dash"></span>Überschrift</div>
    <p class="abs intro-bold" style="left:30px;top:66px;width:490px">Utem aut porumet labore doluptas aliquat ilignias et aut voluptati rem a dipsam eum harumquature quo quis magnameniti optatius delecepra volupis con pere num, ommolor atemoli icimusam quiamus quaepud iatior sum quis amus</p>
    <p class="abs copy" style="left:30px;top:128px;width:230px">Utem aut porumet labore doluptas aliquat ilignias et aut voluptati rem a dipsam eum harumquature quo quis magnameniti optatius delecepra volupis con pere num, ommolor atemoli icimusam quis amus quiamus quaepud iatior sum quis amus iduci as acit ut odigend uciamet. Obita qui to moloresciam ut dolupta comnima gnatatur magnatis voluptas magnis dolupta tincime laces molorrum, omnissus dolor atem aborehenda simuscium ressin corpore pudaest qui d</p>
    <p class="abs copy" style="left:290px;top:128px;width:230px">Utem aut porumet labore doluptas aliquat ilignias et aut voluptati rem a dipsam eum harumquature quo quis magnameniti optatius delecepra volupis con pere num, ommolor atemoli icimusam quiamus quaepud iatior sum quis amus iduci as acit ut odigend uciamet Tem ium, soluptiorem quo cus eum incturio.</p>
    <div class="page-rule" style="left:0;top:352px;width:520px"></div>
    <svg class="page-number" style="left:390px;top:339px" viewBox="0 0 26 26"><polygon points="13,1 24,7 24,19 13,25 2,19 2,7" fill="#1d1d1d"/><text x="13" y="16.5" font-size="9" font-weight="700" fill="#fff" text-anchor="middle" font-family="Arimo, Arial, sans-serif">7</text></svg>
  </div>
</section>

</body>
</html>
```